See Everyday As A SUNkind Horizon

Hello Designers! We need a captivating notebook cover design for our self-development company for people with disabilities. We help people with a diagnosis see everyday as a great adventure than something to ensure. This notebook is to capture the brightness and positivity of everyday, that your struggles are meant for you to overcome. We would like to see designs that follow with our brand (uploaded) and I've also added our logo and kind of notebook as a guide. The final design should be inviting and bright. Use the title "Start Each Morning With Wonder". Will decide the words once the background design is finalized

Notebook Size: 8.5 x 5.75 inches

Hello Designers! I'm extending the deadline to give you an opportunity to submit different and unique designs for the SUNkind HORIZON Journal. I've given feedback to most of you so this is your opportunity to try something new. Looking for clean, inviting and unique designs that use the logo colour scheme (attached -- navy blue, light blue, yellow, black). Preferably front and back cover designs.

Between 25-35 years

Serif
Sans Serif
Decorative
Script

0255a3
fbed22

• -Use colour scheme as per attachment as main colours (can go beyond for contrast ex. pinks/purples/indigo/etc)
• Would like to see designs related to nature, art and/or graphic prints.
• icons (no stick figures), silhouettes of people, no hands
• NO stock images

```html
<!DOCTYPE html>
<html lang="en">
<head>
<meta charset="utf-8">
<title>SUNkind Horizon Journal – Cover</title>
<link rel="stylesheet" href="https://fonts.googleapis.com/css2?family=Roboto+Condensed:wght@700&display=swap">
<style>
  :root {
    --navy: #0255a3;
    --sun: #fbed22;
    --sky: #aecbd9;
    --orange: #f08c00;
    --page: #ffffff;
  }
  html, body {
    margin: 0;
    padding: 0;
    width: 1200px;
    height: 1200px;
    overflow: hidden;
    background: var(--page);
  }
  .cover {
    position: absolute;
    left: 236px;
    top: 62px;
    width: 728px;
    height: 1076px;
    overflow: hidden;
    background: linear-gradient(to right, var(--navy) 0 366px, var(--sun) 366px 100%);
    font-family: "Roboto Condensed", "Arial Narrow", sans-serif;
    font-weight: 700;
  }
  .headline {
    position: absolute;
    right: 24px;
    top: 0;
    width: 720px;
    height: 700px;
    margin: 0;
    transform: skewY(-5deg);
    transform-origin: right top;
    text-align: right;
    text-transform: uppercase;
    font-weight: 700;
  }
  .headline span {
    position: absolute;
    right: 0;
    display: block;
    white-space: nowrap;
    line-height: 0.8;
  }
  .line-start {
    top: 58px;
    font-size: 162px;
    color: var(--sky);
    letter-spacing: -2px;
    text-shadow: -7px 6px 0 var(--navy);
  }
  .line-morning {
    top: 186px;
    font-size: 84px;
    color: var(--navy);
    letter-spacing: -1px;
  }
  .line-with {
    top: 248px;
    font-size: 206px;
    color: var(--orange);
    letter-spacing: -2px;
  }
  .line-wonder {
    top: 384px;
    font-size: 206px;
    color: var(--orange);
    letter-spacing: -2px;
  }
  .brand-name {
    position: absolute;
    right: 26px;
    bottom: 34px;
    margin: 0;
    font-size: 30px;
    color: var(--navy);
    letter-spacing: 0.5px;
  }
</style>
</head>
<body>
  <main class="cover">
    <h1 class="headline" aria-label="Start Each Morning With Wonder">
      <span class="line-start">Start</span>
      <span class="line-morning">Each Morning</span>
      <span class="line-with">With</span>
      <span class="line-wonder">Wonder</span>
    </h1>
    <p class="brand-name">SUNkind Horizon</p>
  </main>
</body>
</html>
```